CLS Business card, letterhead, and stationery, email tag, fax cover
Clear and Professional material
Simple
Léandre Ormessac
Directeur des ventes
47, rue de Valmorin
Paris , 75016
France
leandre@clsys.fr
www.clsys.fr
Logo + tag line
LOGO
SMALL LOGO

```html
<!DOCTYPE html>
<html lang="fr">
<head>
<meta charset="utf-8">
<title>CLS — Carte de visite</title>
<link rel="stylesheet" href="https://fonts.googleapis.com/css2?family=Open+Sans:wght@400;700&family=Tinos&display=swap">
<style>
  :root {
    --page: #e9e7e4;
    --card: #ffffff;
    --cyan: #45bde0;
    --cyan-light: #8fd8ee;
    --grey: #6d6e70;
    --ink: #3c3c3c;
    --rule: #c9c9c9;
  }
  html, body {
    margin: 0;
    width: 1200px;
    height: 852px;
    overflow: hidden;
    background: var(--page);
  }
  .business-card {
    position: absolute;
    left: 100px;
    top: 126px;
    width: 1000px;
    height: 600px;
    background: var(--card);
    border-radius: 34px;
    overflow: hidden;
    box-shadow: 0 6px 24px rgba(0,0,0,0.12);
  }
  .edge-swoosh {
    position: absolute;
    left: 0;
    top: 0;
    width: 1000px;
    height: 600px;
  }
  .brand {
    position: absolute;
    left: 150px;
    top: 60px;
    width: 420px;
  }
  .brand-figure {
    position: absolute;
    left: 0;
    top: 0;
    width: 90px;
    height: 190px;
    border-radius: 45px;
    background: linear-gradient(180deg, #bfc0c2, #8a8b8d);
  }
  .brand-name {
    position: absolute;
    left: 110px;
    top: 48px;
    margin: 0;
    font-family: "Open Sans", sans-serif;
    font-weight: 700;
    font-size: 30px;
    line-height: 1.1;
    color: var(--cyan);
    white-space: nowrap;
  }
  .brand-tagline {
    position: absolute;
    left: 110px;
    top: 130px;
    margin: 0;
    font-family: "Open Sans", sans-serif;
    font-size: 20px;
    color: var(--cyan);
    white-space: nowrap;
  }
  .identity {
    position: absolute;
    right: 470px;
    top: 320px;
    text-align: right;
    font-family: "Tinos", serif;
    color: var(--ink);
  }
  .identity .person {
    margin: 0 0 4px;
    font-family: "Open Sans", sans-serif;
    font-weight: 700;
    font-size: 28px;
    color: var(--cyan);
  }
  .identity .role {
    margin: 0 0 26px;
    font-size: 24px;
  }
  .identity address {
    font-style: normal;
    font-size: 25px;
    line-height: 1.3;
  }
  .divider {
    position: absolute;
    left: 555px;
    top: 305px;
    width: 1px;
    height: 250px;
    background: var(--rule);
  }
  .contacts {
    position: absolute;
    left: 580px;
    top: 305px;
    margin: 0;
    padding: 0;
    list-style: none;
    font-family: "Tinos", serif;
    font-size: 25px;
    color: var(--ink);
  }
  .contacts li {
    display: flex;
    align-items: center;
    height: 44px;
  }
  .contacts svg {
    width: 22px;
    height: 22px;
    margin-right: 16px;
    flex: none;
  }
</style>
</head>
<body>
  <article class="business-card">
    <svg class="edge-swoosh" viewBox="0 0 1000 600" aria-hidden="true">
      <path d="M0 130 C 60 260, 90 430, 230 600 L 0 600 Z" fill="var(--cyan)"/>
      <path d="M0 150 C 45 280, 70 440, 190 600" fill="none" stroke="var(--grey)" stroke-width="12"/>
      <path d="M0 175 C 30 300, 50 450, 150 600 L 0 600 Z" fill="var(--cyan-light)"/>
    </svg>

    <header class="brand">
      <div class="brand-figure" role="img" aria-label="Silhouette de femme stylisée du logo"></div>
      <p class="brand-name">Corvane Lumis Systems</p>
      <p class="brand-tagline">solutions avancées de la peau</p>
    </header>

    <section class="identity">
      <p class="person">Léandre Ormessac</p>
      <p class="role">Directeur des ventes</p>
      <address>47, rue de Valmorin<br>Paris , 75016<br>France</address>
    </section>

    <div class="divider"></div>

    <ul class="contacts">
      <li>
        <svg viewBox="0 0 24 24"><path d="M6 3 L10 3 L11 8 L8.5 9.5 C9.5 12 12 14.5 14.5 15.5 L16 13 L21 14 L21 18 C21 19.5 19.5 21 18 21 C10 20 4 14 3 6 C3 4.5 4.5 3 6 3 Z" fill="var(--cyan)"/></svg>
        01.40.00.00.11
      </li>
      <li>
        <svg viewBox="0 0 24 24"><rect x="6" y="2" width="12" height="20" rx="2" fill="var(--cyan)"/><rect x="8" y="5" width="8" height="11" fill="#fff"/></svg>
        06.00.00.00.22
      </li>
      <li>
        <svg viewBox="0 0 24 24"><rect x="3" y="9" width="18" height="11" rx="2" fill="var(--cyan)"/><rect x="7" y="3" width="10" height="7" fill="var(--cyan)"/><rect x="7" y="14" width="10" height="2" fill="#fff"/></svg>
        01.40.00.00.12
      </li>
      <li>
        <svg viewBox="0 0 24 24"><circle cx="12" cy="12" r="10" fill="var(--cyan)"/><rect x="6" y="8" width="12" height="8" fill="#fff"/><path d="M6 8 L12 13 L18 8" fill="none" stroke="var(--cyan)" stroke-width="1.5"/></svg>
        leandre@clsys.fr
      </li>
      <li>
        <svg viewBox="0 0 24 24"><circle cx="12" cy="12" r="10" fill="var(--cyan)"/><circle cx="12" cy="12" r="6" fill="none" stroke="#fff" stroke-width="1.5"/><line x1="6" y1="12" x2="18" y2="12" stroke="#fff" stroke-width="1.5"/></svg>
        www.clsys.fr
      </li>
    </ul>
  </article>
</body>
</html>
```